KMR (Aust) Auslan 2 page flyer

We require a 2-page flayer advertising our Auslan and Braille signage. We manufacture Braille amentities signage in Australia. See attached brief and copy documents as well as image assets.

Target Market(s)

Schools, local councils (government)

Font styles to use
Sans Serif

Colors
0054AA
0677BA
7BADD7
CADEEF
E8F1F8
0094D4
00A9DD
6FCCEA
C7EBF8
E9F6FB
FFC000
F8CF3A
FAE287
FDF2CF
FEFAEE

```html
<!DOCTYPE html>
<html lang="en">
<head>
<meta charset="utf-8">
<title>KMR (Aust) Auslan Braille Tactile Signs – Range Options</title>
<link href="https://fonts.googleapis.com/css2?family=Montserrat:wght@500;600;700;800;900&family=Open+Sans:wght@400;600;700&display=swap" rel="stylesheet">
<style>
:root{
  --orange:#F7A600;
  --gold:#FFC000;
  --gold-soft:#FDF2CF;
  --ink:#2E2E2E;
  --charcoal:#3C3C3C;
  --grey-line:#C9C9C9;
  --grey-panel:#E6E6E6;
  --text:#444444;
  --blue-dark:#0054AA;
  --blue:#0677BA;
  --blue-light:#7BADD7;
  --blue-pale:#CADEEF;
  --page:#FFFFFF;
  --canvas:#EDEDED;
}
*{box-sizing:border-box;margin:0;padding:0}
html,body{width:1200px;height:4000px;overflow:hidden;background:var(--canvas)}
body{font-family:"Open Sans",Arial,sans-serif;color:var(--text);position:relative}
.page{position:absolute;left:70px;width:1060px;height:1500px;background:var(--page);box-shadow:0 6px 24px rgba(0,0,0,.12);overflow:hidden}
.page--one{top:300px}
.page--two{top:2100px}
.page__body{padding:64px 70px 0}

.title{text-align:center;font-family:"Montserrat",sans-serif;font-weight:900;line-height:1.05}
.title__main{font-size:48px;color:var(--ink);letter-spacing:.5px}
.title__sub{font-size:44px;color:var(--orange)}

.intro{margin-top:28px;background:var(--orange);color:#fff;padding:26px 40px;text-align:center;font-size:16px;line-height:1.55}
.intro p+p{margin-top:14px}

.section{margin-top:30px}
.section__head{display:flex;align-items:center;gap:0;margin-bottom:12px}
.section__label{font-family:"Montserrat",sans-serif;font-weight:800;font-size:22px;color:var(--ink);background:linear-gradient(to top,var(--gold) 0 45%,transparent 45%);padding:0 10px 2px 0;white-space:nowrap}
.section__rule{flex:1;height:2px;background:var(--grey-line);margin-left:6px}
.section p{font-size:15px;line-height:1.6}

.examples{margin-top:22px;background:var(--grey-panel);padding:0 0 26px}
.examples__banner{margin:0 auto;width:520px;background:var(--orange);color:#fff;font-family:"Montserrat",sans-serif;font-weight:800;font-size:26px;text-align:center;padding:10px 0;letter-spacing:.5px}
.examples__art{display:block;margin:22px auto 0;width:760px;height:400px;border-radius:4px;background:linear-gradient(135deg,#cfd3d6 0%,#9ea4a8 40%,#2b2b2b 75%,#6b8fb8 100%)}

.footer{position:absolute;left:0;right:0;bottom:0;height:92px;display:flex;align-items:center;font-size:13px;color:var(--text)}
.footer::after{content:"";position:absolute;left:0;right:0;bottom:0;height:10px;background:var(--gold)}
.footer__phone{height:82px;align-self:flex-start;width:330px;background:var(--charcoal);clip-path:polygon(0 0,100% 0,88% 100%,0 100%);display:flex;align-items:center;gap:12px;padding-left:44px;color:#fff;font-family:"Montserrat",sans-serif;font-weight:700;font-size:28px}
.footer__contact{display:flex;align-items:center;gap:10px;margin-left:40px}
.footer__contact + .footer__contact{margin-left:auto;margin-right:60px}
.footer__icon{width:18px;height:18px;flex:none}
.footer__lines{line-height:1.5;margin-top:-10px}

/* page two */
.tech{display:grid;grid-template-columns:1fr 220px 230px;gap:22px;align-items:start}
.tag{display:inline-block;font-family:"Montserrat",sans-serif;font-weight:800;font-size:19px;color:var(--ink)}
.tag mark{background:var(--gold);color:var(--ink);padding:2px 6px}
.tech p{font-size:15px;line-height:1.5;margin-top:8px}
.tech__fabric{height:140px;background:linear-gradient(135deg,var(--blue-dark),var(--blue-light) 55%,var(--blue-pale))}

.finish{margin-top:36px}
.finish__title{font-family:"Montserrat",sans-serif;font-weight:800;font-size:24px;color:var(--ink)}
.finish__title span{background:linear-gradient(to top,var(--gold) 0 40%,transparent 40%)}
.finish__grid{display:grid;grid-template-columns:1fr 420px;gap:40px;margin-top:14px;align-items:start}
.finish--internal .finish__grid{grid-template-columns:420px 1fr}
.finish--internal .finish__title{text-align:right}
.spec{font-size:14px;line-height:1.5}
.spec dt{font-family:"Montserrat",sans-serif;font-weight:800;color:var(--orange);font-size:14px;margin-top:12px}
.spec dt:first-child{margin-top:0}
.spec dd{margin:0}
.sign-art{height:280px;border:1px solid var(--grey-line);background:linear-gradient(160deg,#f4f4f4,#c9cdd0 60%,#a7adb1)}

.credits{margin-top:36px;display:grid;grid-template-columns:1fr 1fr;gap:30px}
.credits__label{font-family:"Montserrat",sans-serif;font-weight:800;font-size:17px;color:var(--ink)}
.credits__label span{color:var(--orange)}
.credits p{font-size:14px;line-height:1.45;font-weight:600;margin-top:4px}
.studio{display:inline-block;margin-left:10px;font-family:"Open Sans",sans-serif;font-weight:700;font-size:15px;color:var(--orange)}
.partners{display:flex;gap:18px;margin-top:10px}
.partners__badge{width:120px;height:70px;background:var(--blue-pale)}
.partners__badge:nth-child(2){width:70px;border-radius:50%;background:var(--gold-soft)}
.partners__badge:nth-child(3){background:#E9F6FB}

.closing{margin-top:26px;font-size:14px;line-height:1.5;text-align:center}
.photos{margin-top:20px;display:grid;grid-template-columns:repeat(4,1fr);gap:12px}
.photos__item{height:150px;background:linear-gradient(160deg,#7a8a5a,#4c5a38 60%,#8a7a5c)}
</style>
</head>
<body>

<!-- Page 1 -->
<section class="page page--one">
  <div class="page__body">
    <h1 class="title">
      <span class="title__main">AUSLAN BRAILLE TACTILE SIGNS</span><br>
      <span class="title__sub">RANGE OPTIONS</span>
    </h1>

    <div class="intro">
      <p>KMR (Aust) are excited to showcase our exclusive, Auslan Braille Tactile Signs: an interactive learning Alphabet Range.</p>
      <p>This exciting range of 26 or 52 signs offer a durable, fun, educational and interactive set of Alphabetical signs comprising Braille &amp; Tactile lettering and matched with images of the Auslan sign language. Featuring each letter of the alphabet along with a word that identifies activities or landmarks around park and nature environments. Each word is nationally recognised in Auslan and suitable Australia Wide!</p>
    </div>

    <div class="section">
      <div class="section__head"><h2 class="section__label">Where &amp; Why?</h2><span class="section__rule"></span></div>
      <p>If your school, library, council or organisation is interested in the inclusion and education of languages used by people who are blind or have low vision (Braille &amp; Tactile) as well as people who are deaf or have low hearing levels (Auslan), pair the fun and interactive set of signs with your education solution for children and adults alike!</p>
    </div>

    <div class="section">
      <div class="section__head"><h2 class="section__label">Endless Customisations:</h2><span class="section__rule"></span></div>
      <p>Get creative and make this range suited to your school, community and environment, with colours, digital graphics, shapes and backing options suitable for internal or external installation.</p>
    </div>

    <div class="examples">
      <div class="examples__banner">EXAMPLES:</div>
      <div class="examples__art" role="img" aria-label="Photograph of sample Auslan alphabet signs in silver, black and colour finishes with Braille, words and hand sign illustrations"></div>
    </div>

    <div class="section">
      <div class="section__head"><h2 class="section__label">Designing and Ordering:</h2><span class="section__rule"></span></div>
      <p>Contact the friendly Sales Team at KMR (Aust) today on 03 9000 4417 to order your standard set of Auslan Braille Tactile Signs or work with our creative Design Team to create your unique set, suited to your application and requirements.</p>
    </div>
  </div>

  <footer class="footer">
    <div class="footer__phone">
      <svg width="26" height="26" viewBox="0 0 24 24" fill="#fff" aria-hidden="true"><path d="M6.6 10.8a15.1 15.1 0 0 0 6.6 6.6l2.2-2.2a1 1 0 0 1 1-.25 11.4 11.4 0 0 0 3.6.57 1 1 0 0 1 1 1V20a1 1 0 0 1-1 1A17 17 0 0 1 3 4a1 1 0 0 1 1-1h3.5a1 1 0 0 1 1 1c0 1.25.2 2.45.57 3.57a1 1 0 0 1-.25 1z"/></svg>
      +61 3 9000 4417
    </div>
    <div class="footer__contact">
      <svg class="footer__icon" viewBox="0 0 24 24" fill="none" stroke="#F7A600" stroke-width="2" aria-hidden="true"><rect x="3" y="5" width="18" height="14" rx="1"/><path d="M3 6l9 7 9-7"/></svg>
      <div class="footer__lines">sales@kmrtactilesigns.com.au<br>accounts@kmrtactilesigns.com.au</div>
    </div>
    <div class="footer__contact">
      <svg class="footer__icon" viewBox="0 0 24 24" fill="none" stroke="#F7A600" stroke-width="2" aria-hidden="true"><circle cx="12" cy="12" r="9"/><path d="M3 12h18M12 3c3 3 3 15 0 18M12 3c-3 3-3 15 0 18"/></svg>
      <div class="footer__lines" style="margin-top:0">www.kmrtactilesigns.com.au</div>
    </div>
  </footer>
</section>

<!-- Page 2 -->
<section class="page page--two">
  <div class="page__body">
    <div class="tech">
      <div>
        <h2 class="tag">KMR (Aust) Product <mark>Technology:</mark></h2>
        <p>Premium Continuous Surface Encapsulated Polycarbonate Membrane.</p>
      </div>
      <div>
        <h2 class="tag"><mark>Product</mark> Quality:</h2>
        <p>Able to be kept hygienically clean.</p>
      </div>
      <div class="tech__fabric" role="img" aria-label="Close-up photograph of blue polycarbonate membrane surface"></div>
    </div>

    <div class="finish finish--external">
      <h2 class="finish__title">Standard <span>External Finish:</span></h2>
      <div class="finish__grid">
        <dl class="spec">
          <dt>COLOUR:</dt><dd>Black on Silver</dd>
          <dt>BACKING:</dt><dd>3mm Aluminium backing 2.5mm thick overall<br>External Finish: Complete with an Anti Graffiti and UV Stabilising Coating</dd>
          <dt>FIXINGS:</dt><dd>Holes (option)<br>... Endless Customisations...</dd>
        </dl>
        <div class="sign-art" role="img" aria-label="Photograph of silver external Auslan sign showing letter Q, the word Question and a hand sign"></div>
      </div>
    </div>

    <div class="finish finish--internal">
      <h2 class="finish__title">Standard <span>Internal Finish:</span></h2>
      <div class="finish__grid">
        <div class="sign-art" role="img" aria-label="Photograph of silver internal Auslan sign showing the word Ant with Braille and a hand sign"></div>
        <dl class="spec">
          <dt>COLOUR:</dt><dd>Black on Silver</dd>
          <dt>BACKING:</dt><dd>1mm flexible HIPS backing 2.5mm overall<br>Lightweight and smooth to touch.<br>... Endless Customisations...</dd>
          <dt>FIXINGS:</dt><dd>Holes (option)<br>... Endless Customisations...</dd>
        </dl>
      </div>
    </div>

    <div class="credits">
      <div>
        <h3 class="credits__label">INSPIRED <span>BY:</span></h3>
        <p>Signage produced for Birchwood Lower Park,<br>Birchwood Victoria</p>
        <h3 class="credits__label" style="margin-top:20px">ILLUSTRATED <span>BY:</span><span class="studio">Penfold Studio</span></h3>
      </div>
      <div>
        <h3 class="credits__label">A COLLABORATION <span>OF:</span></h3>
        <div class="partners">
          <div class="partners__badge" role="img" aria-label="Greywater Shire Council badge"></div>
          <div class="partners__badge" role="img" aria-label="Partner badge"></div>
          <div class="partners__badge" role="img" aria-label="Hearing Kids Alliance badge"></div>
        </div>
      </div>
    </div>

    <p class="closing">Education and inclusion for all is at the core of KMR (Aust)'s Mission, Vision and Values and we are proud of the successful collaboration between KMR (Aust), Greywater Shire Council and Hearing Kids Alliance.</p>

    <div class="photos">
      <div class="photos__item" role="img" aria-label="Photograph of Auslan sign installed in a park"></div>
      <div class="photos__item" role="img" aria-label="Photograph of Auslan sign on a post in parkland"></div>
      <div class="photos__item" role="img" aria-label="Photograph of park path with installed signage"></div>
      <div class="photos__item" role="img" aria-label="Photograph of Auslan sign mounted near trees"></div>
    </div>
  </div>

  <footer class="footer">
    <div class="footer__phone">
      <svg width="26" height="26" viewBox="0 0 24 24" fill="#fff" aria-hidden="true"><path d="M6.6 10.8a15.1 15.1 0 0 0 6.6 6.6l2.2-2.2a1 1 0 0 1 1-.25 11.4 11.4 0 0 0 3.6.57 1 1 0 0 1 1 1V20a1 1 0 0 1-1 1A17 17 0 0 1 3 4a1 1 0 0 1 1-1h3.5a1 1 0 0 1 1 1c0 1.25.2 2.45.57 3.57a1 1 0 0 1-.25 1z"/></svg>
      +61 3 9000 4417
    </div>
    <div class="footer__contact">
      <svg class="footer__icon" viewBox="0 0 24 24" fill="none" stroke="#F7A600" stroke-width="2" aria-hidden="true"><rect x="3" y="5" width="18" height="14" rx="1"/><path d="M3 6l9 7 9-7"/></svg>
      <div class="footer__lines">sales@kmrtactilesigns.com.au<br>accounts@kmrtactilesigns.com.au</div>
    </div>
    <div class="footer__contact">
      <svg class="footer__icon" viewBox="0 0 24 24" fill="none" stroke="#F7A600" stroke-width="2" aria-hidden="true"><circle cx="12" cy="12" r="9"/><path d="M3 12h18M12 3c3 3 3 15 0 18M12 3c-3 3-3 15 0 18"/></svg>
      <div class="footer__lines" style="margin-top:0">www.kmrtactilesigns.com.au</div>
    </div>
  </footer>
</section>

</body>
</html>
```